Pediatric Vision Care: Myopia Control Brochure

We are a pediatric eye care practice (ophthalmology and optometry). One of our services we offer for children is myopia control, which are strategies for slowing or stopping the progression of nearsightedness. This is a service we need to sell to parents because most insurance won't pay for it. There are different options we offer that can work well for kids in different situations: glasses with Corvane lenses, atropine eye drops, and/or special contact lenses. We need a brochure we can distribute to parents to let them know about this service that would encourage them to buy it for children who need it. Attached is our initial draft brochure created by our staff that provides text that we want to keep. The images and layout can change. We probably need at least one or two photos of kids on the brochure, because this is only something that works for children who are still growing, and the target audience is parents of 4-8 year old children.

Target Market(s)

Parents of 4-8 year old children

Font styles to use
Sans Serif

Requirements
Must have
• I'm uploading our company logo that should be included somewhere on the brochure. You can include contact information (web address, phone number) for our practice that is found on our website: http://www.brookhollowkidsvision.com/
Should not have
• This should not look childish. We need the impression to be friendly but professional, medical, expert.

```html
<!DOCTYPE html>
<html lang="en">
<head>
<meta charset="utf-8">
<title>Brookhollow Kids Vision – Myopia Brochure</title>
<link rel="stylesheet" href="https://fonts.googleapis.com/css2?family=Nunito:wght@400;600;700;800&family=Crimson+Text:ital@1&display=swap">
<style>
:root{
  --stage:#a4a4a4;
  --paper:#ffffff;
  --lavender:#edf0fb;
  --lavender-deep:#dfe4f7;
  --brand-blue:#6878dc;
  --stripe-blue:#6a7bd6;
  --green:#8ccc00;
  --yellow:#f6c81a;
  --orange:#f39200;
  --ink:#1e1e24;
  --ink-soft:#2c2c34;
  --white:#ffffff;
}
*{margin:0;padding:0;box-sizing:border-box}
html,body{width:1200px;height:2435px;overflow:hidden;background:var(--stage)}
body{position:relative;font-family:"Nunito",sans-serif;color:var(--ink)}
.brochure-frame{position:absolute;left:50px;top:793px;width:1100px;height:849px;box-shadow:0 6px 18px rgba(0,0,0,.25)}
.brochure{position:absolute;left:0;top:0;width:1030px;height:795px;transform:scale(1.068);transform-origin:0 0;background:var(--paper);overflow:hidden}
.panel-left{position:absolute;left:0;top:0;width:343px;height:795px;background:var(--lavender)}
.artwork{position:absolute;left:0;top:0;width:1030px;height:795px}
.section-heading{position:absolute;font-weight:700;font-size:20px;line-height:24px;padding-left:11px;border-left:4px solid var(--brand-blue);color:var(--ink)}
.env-heading{left:34px;top:46px}
.env-body{position:absolute;left:46px;top:126px;width:252px;font-size:12.6px;line-height:18px;color:var(--ink-soft)}
.env-body p+p{margin-top:18px}
.girl-photo{position:absolute;left:32px;top:525px;width:280px;height:270px}
.tagline{position:absolute;left:445px;top:40px;font-family:"Crimson Text",serif;font-style:italic;font-size:24px;line-height:26px;color:var(--ink)}
.contact-heading{left:385px;top:392px}
.contact{position:absolute;left:389px;top:470px;font-size:13.4px;line-height:18px;color:var(--ink)}
.contact .office{font-weight:700}
.contact .group{margin-bottom:18px}
.brand-name{position:absolute;left:728px;top:70px;display:flex;align-items:center;gap:10px;font-size:24px;font-weight:400;color:var(--ink)}
.brand-dot{width:16px;height:16px;border-radius:50%;background:var(--brand-blue)}
.cover-title{position:absolute;left:668px;top:615px;width:362px;text-align:center;color:var(--white)}
.cover-title h1{font-weight:700;font-size:28px;line-height:34px}
.cover-title p{margin-top:14px;font-size:15px;line-height:20px;color:#eef0ff}
</style>
</head>
<body>
<div class="brochure-frame">
  <div class="brochure">
    <div class="panel-left"></div>

    <svg class="artwork" viewBox="0 0 1030 795" xmlns="http://www.w3.org/2000/svg">
      <defs>
        <linearGradient id="clinicTones" x1="0" y1="0" x2="1" y2="1">
          <stop offset="0" stop-color="#e6ebef"/>
          <stop offset="0.5" stop-color="#c9d0d6"/>
          <stop offset="1" stop-color="#e9e4de"/>
        </linearGradient>
        <radialGradient id="girlTones" cx="0.5" cy="0.45" r="0.55">
          <stop offset="0" stop-color="#d9a27a"/>
          <stop offset="0.6" stop-color="#b46a3c"/>
          <stop offset="1" stop-color="#edf0fb"/>
        </radialGradient>
      </defs>
      <g role="img" aria-label="Photo of an eye doctor showing an eye model to a young boy in a bright clinic">
        <path d="M430 180 L1030 180 L1030 590 C760 510 500 380 430 180 Z" fill="url(#clinicTones)"/>
      </g>
      <ellipse cx="870" cy="40" rx="300" ry="215" fill="var(--lavender)"/>
      <path d="M668 470 C800 535 940 575 1030 588 L1030 795 L668 795 Z" fill="var(--brand-blue)"/>
      <path d="M356 0 C370 270 520 440 1030 600" fill="none" stroke="var(--stripe-blue)" stroke-width="9"/>
      <path d="M382 0 C395 230 470 350 560 410" fill="none" stroke="var(--green)" stroke-width="16"/>
      <path d="M560 410 C610 445 660 468 700 480" fill="none" stroke="var(--yellow)" stroke-width="14"/>
      <path d="M700 480 C820 530 940 565 1030 585" fill="none" stroke="var(--orange)" stroke-width="6"/>
      <g role="img" aria-label="Portrait photo of a smiling girl wearing glasses">
        <rect x="32" y="525" width="280" height="270" fill="url(#girlTones)"/>
      </g>
    </svg>

    <h2 class="section-heading env-heading">Environmental<br>Options</h2>
    <div class="env-body">
      <p>All myopic children can benefit from these lifestyle changes. It is important to get your child outdoors consistently. There is strong evidence that children who spend at least 2 hours a day outdoors are less likely to become myopic, and their myopia progresses slower than children who are outdoors less. Some studies show that increasing outdoor time by as few as 45 min a day is beneficial in reducing progression.</p>
      <p>There is some evidence that consistent use of screens, particularly held very close to the face, can worsen nearsightedness. We recommend limiting non academic screen time and near work, and encourage your child to use the 20-20-20 rule. Every 20 minutes take a 20 second break to look at least 20 feet away.</p>
    </div>

    <p class="tagline">Every child<br>deserves to see<br>the world clearly</p>

    <div class="brand-name"><span class="brand-dot"></span>Brookhollow Kids Vision</div>

    <h2 class="section-heading contact-heading">Contact<br>with us</h2>
    <div class="contact">
      <div class="group">Voice : (555) 214-0050<br>Text : (555) 388-3003<br>Fax : (555) 214-4538</div>
      <div class="group"><span class="office">Harbor Point Office</span><br>Brookhollow Kids Vision<br>2180 Alder Grove Avenue<br>Harbor Point, VA 23999</div>
      <div class="group"><span class="office">Millbrook Office</span><br>870 Lantern Way<br>Millbrook, VA 23811</div>
      <div>www.brookhollowkidsvision.com<br>appointments@brookhollowkidsvision.com</div>
    </div>

    <div class="cover-title">
      <h1>Protecting Young<br>Eyes from Myopia</h1>
      <p>Early detection and effective<br>management for lifelong<br>visual health.</p>
    </div>
  </div>
</div>
</body>
</html>
```